Online media outlet needs a blog and logo

A new online blog platform is being established in the UK. The blog will be very similar in layout to www.lumvero.co. It will need to have a main story slider showing three slides and block tiles beneath the slider for additional tiles.

The blog platform will be called 'Brisket Lantern' and will also need a professional looking logo design for the name.

The website should be designed in Word Press.

Industry/Entity Type

Media

Logo Text

Brisket Lantern

Coding

Coded - Design and coding required

Number of Pages Required

3 page

Font styles to use
Other font styles liked:
• Helvetica

Requirements
Must have
• A slider showing three slides. Be similar to Lum V (see previous comment). Be Word Press compatible.

```html
<!DOCTYPE html>
<html lang="en">
<head>
<meta charset="utf-8">
<title>Brisket Lantern</title>
<link href="https://fonts.googleapis.com/css2?family=Raleway:ital,wght@0,400;0,500;0,600;0,700;1,400&display=swap" rel="stylesheet">
<style>
:root{
  --ink:#222;
  --muted:#666;
  --faint:#999;
  --bar:#2b2b2b;
  --bar-dark:#111;
  --page:#efefef;
  --card:#fff;
  --accent:#29a9e1;
  --sky:#5bb8e8;
  --violet:#6a5cd6;
  --green:#5cc45c;
  --yellow:#f1c40f;
  --footer:#151515;
}
*{box-sizing:border-box;margin:0;padding:0}
html,body{width:677px;height:1200px;overflow:hidden}
body{font-family:'Raleway',Helvetica,Arial,sans-serif;color:var(--ink);background:var(--page);position:relative}
.abs{position:absolute}

.hero{left:0;top:0;width:677px;height:370px;background:linear-gradient(100deg,#6e5a48 0%,#8a7a6a 35%,#c9c2ba 62%,#e8e4df 100%)}
.masthead{left:0;top:0;width:677px;height:38px;background:rgba(20,20,20,.72)}
.brand{left:50px;top:9px;color:#fff;font-size:18px;font-weight:400;letter-spacing:.3px}
.social{left:498px;top:12px;display:flex;gap:5px}
.social span{width:14px;height:14px;border-radius:50%;background:#fff}
.menu{left:581px;top:13px;color:#fff;font-size:8px;display:flex;align-items:center;gap:6px}
.menu svg{display:block}

.story{left:48px;top:178px;width:222px;height:138px;background:rgba(40,40,40,.72);border-radius:2px;padding:18px 16px;color:#fff}
.story .kicker{font-size:8px;letter-spacing:.3px;margin-bottom:9px;display:flex;align-items:center;gap:5px}
.story h1{font-size:12.5px;font-weight:700;line-height:1.4;margin-bottom:10px}
.story p{font-size:8.2px;line-height:1.9;color:#ddd;margin-bottom:6px}
.story a{font-size:8.5px;font-weight:700;color:var(--accent);text-decoration:none}

.topics{left:0;top:370px;width:677px;height:51px;background:var(--bar);display:flex;padding-left:49px}
.topics a{color:#fff;text-decoration:none;font-size:9.5px;display:flex;align-items:center;justify-content:center;border-right:1px solid #3c3c3c;height:51px}
.topics a.active{background:var(--bar-dark)}

.card{background:var(--card);border-top:3px solid var(--sky);box-shadow:0 1px 2px rgba(0,0,0,.15);overflow:hidden}
.card .photo{position:absolute}
.tag{position:absolute;background:rgba(30,30,30,.75);color:#fff;font-size:8.5px;font-weight:600;padding:3px 6px}
.body{position:absolute;padding:0 12px}
.body h2{font-size:9.4px;font-weight:700;line-height:1.45;color:var(--ink)}
.date{font-size:6.6px;font-style:italic;color:var(--faint);margin-top:4px}
.rule{border-top:1px solid #e6e6e6;margin:8px 0 7px}
.excerpt{font-size:7.3px;line-height:1.78;color:var(--muted)}
.share{display:flex;align-items:center;gap:8px;font-size:6.2px;color:#444;margin-top:9px}
.share i{display:block;width:7px;height:7px;border-radius:50%;background:#222}

.newsletter{left:0;top:994px;width:677px;height:174px;background:linear-gradient(180deg,#3a3a3a,#2a2a2a 60%,#1f1f1f);text-align:center;color:#fff}
.newsletter h3{font-size:21px;font-weight:400;margin-top:39px}
.newsletter p{font-size:10.4px;margin-top:8px;color:#e8e8e8}
.field{position:absolute;top:101px;height:27px;background:#fff;font-size:8.8px;color:#888;display:flex;align-items:center;padding:0 10px}
.subscribe{position:absolute;left:495px;top:101px;width:70px;height:27px;background:var(--accent);color:#fff;font-size:8.5px;font-weight:700;display:flex;align-items:center;justify-content:center}
.footer{left:0;top:1168px;width:677px;height:32px;background:var(--footer);color:#ddd;font-size:7.6px;display:flex;align-items:center;justify-content:center;border-top:1px solid #333}
.footer b{color:#fff;font-weight:700;margin:0 3px}
</style>
</head>
<body>

<div class="abs hero" role="img" aria-label="Photo of a smiling businesswoman in a white blazer in front of blurred bookshelves"></div>

<header class="abs masthead"></header>
<div class="abs brand">BRISKET LANTERN</div>
<div class="abs social"><span></span><span></span><span></span><span></span></div>
<div class="abs menu">MENU
  <svg width="12" height="9" viewBox="0 0 12 9"><rect y="0" width="12" height="1.4" fill="#fff"/><rect y="3.8" width="12" height="1.4" fill="#fff"/><rect y="7.6" width="12" height="1.4" fill="#fff"/></svg>
</div>

<article class="abs story">
  <div class="kicker"><svg width="7" height="7" viewBox="0 0 7 7"><path d="M1 6 L1.5 4.2 L4.6 1.1 L5.9 2.4 L2.8 5.5 Z" fill="#fff"/></svg>BREAKING NEWS</div>
  <h1>Lorem ipsum dolor sit amet, consectetuer adipiscing</h1>
  <p>Lorem ipsum dolor sit amet, consectetuer adipiscing elit, sed diam nonummy nibh [...]</p>
  <a href="#">READ MORE</a>
</article>

<nav class="abs topics">
  <a class="active" href="#" style="width:109px">CURRENT TOPICS</a>
  <a href="#" style="width:98px">GOVERNMENT</a>
  <a href="#" style="width:78px">POLITICS</a>
  <a href="#" style="width:95px">COMPETITION</a>
  <a href="#" style="width:95px">INVESTMENT</a>
  <a href="#" style="width:104px">SHARE MARKET</a>
</nav>

<!-- Breaking news tall card -->
<article class="abs card" style="left:49px;top:454px;width:185px;height:327px;border-top-color:var(--sky)">
  <div class="photo" role="img" aria-label="Photo of a firefighter spraying a burning car" style="left:0;top:0;width:185px;height:155px;background:linear-gradient(90deg,#6b6a62,#9a8a70 40%,#e07a20 70%,#3a3330)"></div>
  <span class="tag" style="right:5px;top:14px">Breaking News</span>
  <div class="body" style="left:0;top:166px;width:185px">
    <h2>Lorem ipsum dolor sit amet, consectetuer adipiscing elit, sed</h2>
    <div class="date">Posted On 03 May, 2016</div>
    <div class="rule"></div>
    <p class="excerpt">Lorem ipsum dolor sit amet, consectetuer adipiscing elit, sed diam nonummy nibh euismod tincidunt ut laoreet dolore magna aliquam erat volutpat. Ut wisi enim ad minim veniam, quis nostrud exerci tation sed diam nonummy nibh euismod</p>
    <div class="share">SHARE THIS: <i></i><i></i></div>
  </div>
</article>

<!-- Politics card -->
<article class="abs card" style="left:246px;top:454px;width:185px;height:158px;border-top-color:var(--violet)">
  <div class="photo" role="img" aria-label="Photo of men in suits at a meeting table" style="left:0;top:0;width:185px;height:78px;background:linear-gradient(90deg,#4a3a2c,#8a6a4a 50%,#c8b090)"></div>
  <span class="tag" style="right:5px;top:14px">Politics</span>
  <div class="body" style="left:0;top:88px;width:185px">
    <h2>Lorem ipsum dolor sit amet, consectetuer adipiscing elit, sed</h2>
    <div class="date">Posted On 03 May, 2016</div>
    <div class="share" style="margin-top:12px">SHARE THIS: <i></i><i></i></div>
  </div>
</article>

<!-- Investment card -->
<article class="abs card" style="left:442px;top:454px;width:186px;height:158px;border-top-color:var(--green)">
  <div class="photo" role="img" aria-label="Photo of hands reviewing financial charts on paper" style="left:0;top:0;width:186px;height:78px;background:linear-gradient(160deg,#e6e8ea,#b8c2cc 60%,#7c95b3)"></div>
  <span class="tag" style="right:5px;top:14px">Investment</span>
  <div class="body" style="left:0;top:88px;width:186px">
    <h2>Lorem ipsum dolor sit amet, consectetuer adipiscing elit, sed</h2>
    <div class="date">Posted On 03 May, 2016</div>
    <div class="share" style="margin-top:12px">SHARE THIS: <i></i><i></i></div>
  </div>
</article>

<!-- Entertainment wide card -->
<article class="abs card" style="left:246px;top:622px;width:382px;height:159px;border-top-color:var(--yellow)">
  <div class="photo" role="img" aria-label="Photo of a singer performing with a microphone against a green backdrop" style="left:0;top:0;width:185px;height:159px;background:linear-gradient(135deg,#3a5a2a,#6a8a3a 50%,#2a3a1a)"></div>
  <span class="tag" style="left:104px;top:19px">Entertainment</span>
  <div class="body" style="left:185px;top:12px;width:197px">
    <h2>Lorem ipsum dolor sit amet, consec tetuer adipiscing elit, sed</h2>
    <div class="date">Posted On 03 May, 2016</div>
    <div class="rule"></div>
    <p class="excerpt">Lorem ipsum dolor sit amet, consectetuer adipiscing elit, sed diam nonummy nibh euismod tincidunt ut laoreet dolore magna aliquam erat volutpat. Ut wisi enim ad minim veniam, quis nostrud exerci tation sed diam nonummy nibh</p>
    <div class="share">SHARE THIS: <i></i><i></i></div>
  </div>
</article>

<!-- Share market wide card -->
<article class="abs card" style="left:49px;top:792px;width:382px;height:158px;border-top-color:var(--green)">
  <div class="photo" role="img" aria-label="Photo of a blue stock market chart on a screen" style="left:0;top:0;width:185px;height:158px;background:linear-gradient(135deg,#0a1a5a,#1a4ab0 55%,#0a2070)"></div>
  <span class="tag" style="left:104px;top:19px">Share Market</span>
  <div class="body" style="left:185px;top:12px;width:197px">
    <h2>Lorem ipsum dolor sit amet, consec teteur adipiscing elit, sed</h2>
    <div class="date">Posted On 03 May, 2016</div>
    <div class="rule"></div>
    <p class="excerpt">Lorem ipsum dolor sit amet, consectetuer adipiscing elit, sed diam nonummy nibh euismod tincidunt ut laoreet dolore magna aliquam erat volutpat. Ut wisi enim ad minim veniam, quis nostrud exerci tation sed diam nonummy nibh</p>
    <div class="share">SHARE THIS: <i></i><i></i></div>
  </div>
</article>

<!-- Property card -->
<article class="abs card" style="left:442px;top:792px;width:186px;height:158px;border-top-color:var(--sky)">
  <div class="photo" role="img" aria-label="Aerial photo of a coastal city skyline" style="left:0;top:0;width:186px;height:78px;background:linear-gradient(180deg,#a8c4d8,#7a8c94 50%,#4a5a60)"></div>
  <span class="tag" style="right:5px;top:16px">Property</span>
  <div class="body" style="left:0;top:88px;width:186px">
    <h2>Lorem ipsum dolor sit amet, consectetuer adipiscing elit, sed</h2>
    <div class="date">Posted On 03 May, 2016</div>
    <div class="share" style="margin-top:12px">SHARE THIS: <i></i><i></i></div>
  </div>
</article>

<section class="abs newsletter" role="img" aria-label="Newsletter band over a dark city skyline photo">
  <h3>Brisket Lantern Newsletter Sign Up</h3>
  <p>Sign up to our email briefings to have the best of popular capitalism delivered direct to your inbox.</p>
  <div class="field" style="left:113px;width:264px">Email Address</div>
  <div class="field" style="left:386px;width:100px;justify-content:space-between">Daily
    <svg width="9" height="6" viewBox="0 0 9 6"><path d="M1 1 L4.5 4.5 L8 1" stroke="#555" stroke-width="1.2" fill="none"/></svg>
  </div>
  <div class="subscribe">SUBSCRIBE</div>
</section>

<footer class="abs footer">Copright © 2016 <b>Brisket Lantern</b> | All Rights Reserved.</footer>

</body>
</html>
```